Somebody commencing retirement at age 67 and wanting a card to introduce myself

Something that depicts the activities I intend to pursue in retirement: Travel, Golf (both in Australia and internationally), wining (red) and dining and generally leading a decadent lifestyle with my wife (or by myself as appropriate).

I offer no services, but intend to have a decadent, relaxing
retirement, playing golf, drinking red wine and dining at good
restaurants!

The card needs to have a suitably designed logo that reflects the
foregoing.

Requirements
Must have
• On the front of the card, my photograph (attached and cropped as
• appropriate), my name (Carl Brimstead), my mobile phone number (+61 417
• 532 148), my email address (carl@brimstead.example.au) and my residential
• address (41 Kestrel Lane, Marlowe Heights, Western Australia 6031,
• Australia).
• The rear of the card should have my postal address (Carl Brimstead
• Post Office Box 518 Dunmore Western Australia 6947, Australia.)._

```html
<!DOCTYPE html>
<html lang="en">
<head>
<meta charset="utf-8">
<title>Carl Brimstead – Business Card</title>
<link href="https://fonts.googleapis.com/css2?family=Cinzel:wght@500&family=Tinos&display=swap" rel="stylesheet">
<style>
  :root {
    --canvas: #2a2a2a;
    --card-dark: #231f20;
    --card-light: #ffffff;
    --ink: #1a1a1a;
    --ink-light: #f4f4f4;
    --red: #e31e2a;
    --blue: #1aa6e6;
    --purple: #63458a;
    --photo-top: #5a4a44;
    --photo-bottom: #1f2433;
  }
  * { margin: 0; padding: 0; box-sizing: border-box; }
  html, body { width: 1200px; height: 1200px; overflow: hidden; background: var(--canvas); }
  .stage { position: relative; width: 1200px; height: 1200px; }

  .card {
    position: absolute; left: 180px; width: 840px; height: 480px;
    border-radius: 22px; overflow: hidden;
    box-shadow: 0 14px 30px rgba(0,0,0,.45);
  }
  .card--back { top: 70px; background: var(--card-dark); }
  .card--front { top: 630px; background: var(--card-light); }

  .brand-mark { display: flex; align-items: center; gap: 14px; }
  .brand-mark__dot { width: 46px; height: 46px; border-radius: 50%; background: var(--purple); }
  .brand-mark__name {
    font-family: "Cinzel", serif; font-weight: 500; font-size: 34px; letter-spacing: 3px;
  }

  .card--back .brand-mark { position: absolute; top: 120px; left: 0; right: 0; justify-content: center; }
  .card--back .brand-mark__name { color: var(--ink-light); }
  .back-name {
    position: absolute; top: 250px; left: 0; right: 0; text-align: center;
    font-family: "Cinzel", serif; font-weight: 500; font-size: 38px; letter-spacing: 3px; color: var(--ink-light);
  }
  .back-address {
    position: absolute; top: 310px; left: 0; right: 0; text-align: center;
    font-family: "Tinos", serif; font-size: 21px; color: var(--ink-light);
  }

  .front-art { position: absolute; inset: 0; width: 840px; height: 480px; }
  .card--front .brand-mark { position: absolute; top: 90px; left: 60px; }
  .card--front .brand-mark__name { color: var(--ink); }
  .front-name {
    position: absolute; top: 215px; left: 60px;
    font-family: "Cinzel", serif; font-weight: 500; font-size: 40px; letter-spacing: 3px; color: var(--ink);
  }
  .contact-list { position: absolute; top: 285px; left: 60px; list-style: none; }
  .contact-list li {
    display: flex; align-items: flex-start; gap: 14px; margin-bottom: 10px;
    font-family: "Tinos", serif; font-size: 23px; line-height: 30px; color: var(--ink);
  }
  .contact-icon {
    flex: none; width: 30px; height: 30px; border-radius: 50%; background: var(--red);
    display: flex; align-items: center; justify-content: center;
  }
  .contact-icon svg { width: 16px; height: 16px; }
</style>
</head>
<body>
<main class="stage">

  <section class="card card--back" aria-label="Card back">
    <div class="brand-mark">
      <span class="brand-mark__dot"></span>
      <span class="brand-mark__name">Brimstead</span>
    </div>
    <h2 class="back-name">Carl Brimstead</h2>
    <p class="back-address">Post Office Box 518 Dunmore Western Australia 6947, Australia</p>
  </section>

  <section class="card card--front" aria-label="Card front">
    <svg class="front-art" viewBox="0 0 840 480" aria-hidden="false">
      <defs>
        <linearGradient id="portrait-tone" x1="0" y1="0" x2="0" y2="1">
          <stop offset="0" stop-color="var(--photo-top)"/>
          <stop offset="1" stop-color="var(--photo-bottom)"/>
        </linearGradient>
      </defs>
      <path class="swoosh swoosh--red" fill="var(--red)"
            d="M360 0 L450 0 C570 60 620 180 585 300 C565 190 490 80 360 0 Z"/>
      <path class="panel panel--dark" fill="var(--card-dark)"
            d="M545 0 C665 90 655 320 380 480 L840 480 L840 0 Z"/>
      <path class="swoosh swoosh--blue" fill="var(--blue)"
            d="M480 0 L535 0 C655 85 650 300 470 410 C595 300 590 115 480 0 Z"/>
      <g role="img" aria-label="Portrait photograph of Carl Brimstead in a dark suit, arms crossed">
        <rect x="555" y="120" width="270" height="360" rx="4" fill="url(#portrait-tone)"/>
      </g>
    </svg>

    <div class="brand-mark">
      <span class="brand-mark__dot"></span>
      <span class="brand-mark__name">Brimstead</span>
    </div>
    <h1 class="front-name">Carl Brimstead</h1>
    <ul class="contact-list">
      <li>
        <span class="contact-icon"><svg viewBox="0 0 16 16"><path fill="#fff" d="M4 1.5 L6 4.5 L4.8 6 C5.6 8 7.8 10.3 10 11.2 L11.5 10 L14.5 12 L13 14.5 C7 14 2 9 1.5 3 Z"/></svg></span>
        <span>+61 417- 532 148</span>
      </li>
      <li>
        <span class="contact-icon"><svg viewBox="0 0 16 16"><rect x="2" y="4" width="12" height="8" fill="#fff"/><path d="M2 4 L8 9 L14 4" fill="none" stroke="var(--red)" stroke-width="1.2"/></svg></span>
        <span>carl@brimstead.example.au</span>
      </li>
      <li>
        <span class="contact-icon"><svg viewBox="0 0 16 16"><path fill="#fff" d="M8 1 C5 1 3 3.2 3 6 C3 9.5 8 15 8 15 C8 15 13 9.5 13 6 C13 3.2 11 1 8 1 Z"/><circle cx="8" cy="6" r="2" fill="var(--red)"/></svg></span>
        <span>41 Kestrel Lane, Marlowe Heights<br>Western Australia 6031, Australia</span>
      </li>
    </ul>
  </section>

</main>
</body>
</html>
```